Corporate Design für eine Rechtsanwaltskanzlei
Zielgruppe
Ich gründe eine Rechtsanwaltskanzlei.
In der Kanzlei wird auch Mediation als außergerichtliches Konfliktlösungsverfahren angeboten.
Die Kanzlei wird in einer ländlichen Umgebung eröffnet.
Sie bietet zugleich jedoch eine vollständige digitale Aktenbearbeitung und Kommunikation per E-Mail, Videokonferenz an und ist damit ortsungebunden.
Aufgabenstellung
Ich suche ein Design, dass zum einen Seriosität und Kompetenz vermittelt, wie es klassischerweise von einer Rechtsanwältin erwartet wird.
Zum anderen soll das Design aber auch Moderne und Dynamik vermitteln und damit eine deutschlandweite Zielgruppe von Mandanten ansprechen, die gern eine modernere Form der Rechtsberatung mit unkomplizierten Kommunikationswegen wie z.B. per Videokonferenz, Telefon und Email nutzen wollen.
Das Design soll Vertrauen ausstrahlen, sich aber auch von den üblichen typischen Kanzleidesigns abheben und nicht zu bieder wirken.

```html
<!DOCTYPE html>
<html lang="de">
<head>
<meta charset="utf-8">
<title>Marlene Osterwald – Geschäftsausstattung</title>
<link href="https://fonts.googleapis.com/css2?family=Barlow+Semi+Condensed:wght@300;400;600&family=Josefin+Sans:wght@300;400&display=swap" rel="stylesheet">
<style>
  :root {
    --bg: #eeeeef;
    --paper: #ffffff;
    --navy: #03275a;
    --slate: #6b7f8f;
    --rule: #8a98a6;
    --ink: #1c1c1f;
    --gold: #d9a514;
  }
  * { margin: 0; padding: 0; box-sizing: border-box; }
  html, body { width: 821px; height: 1200px; overflow: hidden; background: var(--bg); }
  body { position: relative; font-family: "Barlow Semi Condensed", sans-serif; color: var(--ink); }

  .letterhead {
    position: absolute; left: 89px; top: 45px; width: 642px; height: 908px;
    background: var(--paper); box-shadow: 0 1px 3px rgba(0,0,0,.25);
  }
  .letterhead__rule { position: absolute; left: 356px; right: 0; top: 42px; height: 1px; background: var(--rule); }
  .fold-mark { position: absolute; left: 0; width: 12px; height: 1px; background: var(--rule); }

  .wordmark { position: absolute; text-align: center; font-family: "Josefin Sans", sans-serif; font-weight: 300; color: var(--slate); }
  .wordmark__name { display: block; white-space: nowrap; line-height: 1; }
  .wordmark__role { display: block; white-space: nowrap; line-height: 1; }

  .letterhead .wordmark { left: 358px; width: 252px; top: 108px; }
  .letterhead .wordmark__name { font-size: 19px; letter-spacing: .03em; }
  .letterhead .wordmark__role { font-size: 11px; letter-spacing: .15em; margin-top: 10px; }

  .sender-line { position: absolute; left: 62px; top: 140px; font-size: 7px; letter-spacing: .02em; }

  .contact-block {
    position: absolute; right: 34px; top: 184px; padding-right: 10px;
    border-right: 1px solid var(--rule);
    text-align: right; font-size: 10.8px; font-weight: 300; line-height: 14px; letter-spacing: .03em;
    font-style: normal;
  }
  .contact-block h3 { font-size: 10.8px; font-weight: 600; margin-top: 22px; }
  .contact-block h3.caps { letter-spacing: .05em; margin-top: 12px; }

  .card { position: absolute; top: 987px; width: 260px; height: 168px; box-shadow: 0 1px 3px rgba(0,0,0,.3); }
  .card--front { left: 139px; background: var(--navy); }
  .card--front .wordmark { left: 0; right: 0; top: 70px; color: var(--gold); font-weight: 400; }
  .card--front .wordmark__name { font-size: 15px; letter-spacing: .03em; }
  .card--front .wordmark__role { font-size: 8.6px; letter-spacing: .14em; margin-top: 7px; }

  .card--back { left: 406px; background: var(--paper); border: 1px solid var(--rule); }
  .card--back .wordmark { left: 16px; width: 150px; top: 40px; }
  .card--back .wordmark__name { font-size: 12px; letter-spacing: .02em; }
  .card--back .wordmark__role { font-size: 6.9px; letter-spacing: .08em; margin-top: 6px; }
  .card__contact {
    position: absolute; right: 14px; top: 83px; text-align: right;
    font-size: 7.4px; line-height: 10.8px; letter-spacing: .03em; font-style: normal;
  }
  .card__contact .web { margin-top: 4px; line-height: 11.6px; }
  .card__rule { position: absolute; left: 154px; right: 0; bottom: 12px; height: 1px; background: var(--rule); }
</style>
</head>
<body>

<section class="letterhead">
  <div class="letterhead__rule"></div>
  <span class="fold-mark" style="top:323px"></span>
  <span class="fold-mark" style="top:484px"></span>
  <span class="fold-mark" style="top:644px"></span>

  <div class="wordmark">
    <span class="wordmark__name">MARLENE OSTERWALD</span>
    <span class="wordmark__role">RECHTSANWÄLTIN &amp; MEDIATORIN</span>
  </div>

  <p class="sender-line">NAME COMPANY • Street street 00000 City</p>

  <address class="contact-block">
    Street Street Street<br>
    00000 City<br>
    Tel: +34 (0) 0000 – 000 000<br>
    Movil: +34 000 000 000<br>
    Fax: +34 (0) 0000 – 000 000<br>
    info@namecompany.com<br>
    www.namecompany.com
    <h3>Bürozeiten</h3>
    Montag bis Donnerstag:<br>
    08:00 – 12:30 Uhr und<br>
    14:00 bis 17:30 Uhr<br>
    Freitag:<br>
    08:00 – 12:30 Uhr und<br>
    14:00 bis 16:00 Uhr<br>
    sowie nach Vereinbarung
    <h3 class="caps">FINANZAMT</h3>
    St--Nr- 000/0000/0000<br>
    USt-Id DE000000000
    <h3 class="caps">BANKVERBINDUNG</h3>
    Name of the Bank<br>
    BLZ 000 000 00 – Kto. 00 000 00<br>
    IBAN DE00000000000000000000<br>
    BIC/SWIFT-Code DEAAAAAAAAA
  </address>
</section>

<section class="card card--front">
  <div class="wordmark">
    <span class="wordmark__name">MARLENE OSTERWALD</span>
    <span class="wordmark__role">RECHTSANWÄLTIN &amp; MEDIATORIN</span>
  </div>
</section>

<section class="card card--back">
  <div class="wordmark">
    <span class="wordmark__name">MARLENE OSTERWALD</span>
    <span class="wordmark__role">RECHTSANWÄLTIN &amp; MEDIATORIN</span>
  </div>
  <address class="card__contact">
    Street Street Street<br>
    00000 City<br>
    Tel: +34 (0) 0000 – 000 000<br>
    Movil: +34 000 000 000
    <div class="web">info@namecompany.com<br>www.namecompany.com</div>
  </address>
  <div class="card__rule"></div>
</section>

</body>
</html>
```